kestrova business cards

Hey design gurus!
I'm after a clean, modern, stylish business card for my about to be launched company.
I've uploaded the logos for my company "Kestrova Electrical Solutions"
and also the tarrow alliance logo to whom i am associated.

```html
<!DOCTYPE html>
<html lang="en">
<head>
<meta charset="utf-8">
<title>Kestrova Electrical Solutions – Business Cards</title>
<link rel="stylesheet" href="https://fonts.googleapis.com/css2?family=Montserrat:wght@400;500;700;800&display=swap">
<style>
  :root {
    --bg: #3a3b3d;
    --brand-blue: #1583cf;
    --bright-blue: #1a9ae0;
    --navy: #0b1c2b;
    --navy-deep: #03101a;
    --ink: #1e2228;
    --rule: #5a5f66;
    --badge-red: #b4483a;
    --white: #ffffff;
  }
  * { margin: 0; padding: 0; box-sizing: border-box; }
  html, body { width: 1200px; height: 1200px; overflow: hidden; }
  body {
    background: var(--bg);
    font-family: "Montserrat", sans-serif;
    display: flex;
    flex-direction: column;
    align-items: center;
    justify-content: center;
    gap: 60px;
  }
  .card {
    position: relative;
    width: 840px;
    height: 480px;
    border-radius: 34px;
    overflow: hidden;
  }
  /* Front */
  .card-front { background: linear-gradient(180deg, #ffffff 0%, #f4f5f6 100%); }
  .front-brand {
    position: absolute; left: 70px; top: 74px;
    display: flex; align-items: center; gap: 20px;
  }
  .brand-dot {
    width: 74px; height: 74px; border-radius: 50%;
    border: 8px solid var(--brand-blue);
  }
  .brand-name {
    font-weight: 800; color: var(--brand-blue);
    font-size: 60px; letter-spacing: 2px; text-transform: uppercase;
  }
  .partner-badge {
    position: absolute; left: 335px; top: 172px;
    width: 142px; height: 56px;
    border: 1.5px solid var(--badge-red); border-radius: 8px;
    display: flex; align-items: center; padding-left: 14px;
  }
  .partner-badge .badge-mark {
    width: 40px; height: 34px; background: var(--navy); border-radius: 3px;
  }
  .divider {
    position: absolute; left: 470px; top: 268px;
    width: 1px; height: 118px; background: var(--rule);
  }
  .contact-list {
    position: absolute; left: 515px; top: 240px;
    list-style: none; color: var(--ink); font-size: 18px; line-height: 1.35;
  }
  .contact-list li { display: flex; align-items: flex-start; gap: 12px; }
  .contact-list svg { width: 20px; height: 20px; flex: none; margin-top: 2px; fill: var(--brand-blue); }
  .person { position: absolute; left: 90px; top: 320px; }
  .person-name { color: var(--brand-blue); font-weight: 500; font-size: 32px; letter-spacing: -0.5px; }
  .person-role { color: var(--ink); font-size: 18px; letter-spacing: 0.5px; }
  .front-bands { position: absolute; left: 0; bottom: 0; width: 840px; height: 120px; }
  /* Back */
  .card-back {
    background: radial-gradient(ellipse at 45% 40%, #10273a 0%, var(--navy-deep) 75%);
    display: flex; flex-direction: column; align-items: center; justify-content: center;
  }
  .back-mark {
    width: 120px; height: 120px; border-radius: 50%;
    border: 10px solid var(--bright-blue); margin-bottom: 26px;
  }
  .back-name {
    font-weight: 800; color: var(--bright-blue);
    font-size: 78px; letter-spacing: 3px; text-transform: uppercase; line-height: 1;
  }
  .back-tagline {
    font-weight: 800; color: var(--bright-blue);
    font-size: 22px; letter-spacing: 7px; text-transform: uppercase; margin-top: 12px;
  }
</style>
</head>
<body>
  <section class="card card-front">
    <div class="front-brand">
      <span class="brand-dot"></span>
      <span class="brand-name">Kestrova</span>
    </div>
    <div class="partner-badge" role="img" aria-label="Tarrow Alliance partner badge">
      <span class="badge-mark"></span>
    </div>
    <div class="divider"></div>
    <ul class="contact-list">
      <li><svg viewBox="0 0 24 24"><path d="M6.6 10.8a15 15 0 0 0 6.6 6.6l2.2-2.2c.3-.3.7-.4 1-.2 1.1.4 2.3.6 3.6.6.6 0 1 .4 1 1V20c0 .6-.4 1-1 1A17 17 0 0 1 3 4c0-.6.4-1 1-1h3.5c.6 0 1 .4 1 1 0 1.3.2 2.5.6 3.6.1.3 0 .7-.2 1z"/></svg>(000) 000 0000</li>
      <li><svg viewBox="0 0 24 24"><path d="M2 5h20v14H2z M3 6l9 7 9-7" fill="none" stroke="#1583cf" stroke-width="2"/></svg>email@company.com</li>
      <li><svg viewBox="0 0 24 24"><circle cx="12" cy="12" r="9" fill="none" stroke="#1583cf" stroke-width="2"/><path d="M3 12h18M12 3c3 3 3 15 0 18M12 3c-3 3-3 15 0 18" fill="none" stroke="#1583cf" stroke-width="1.5"/></svg>www.company.com</li>
      <li><svg viewBox="0 0 24 24"><path d="M12 2a7 7 0 0 0-7 7c0 5 7 13 7 13s7-8 7-13a7 7 0 0 0-7-7zm0 9.5A2.5 2.5 0 1 1 12 6a2.5 2.5 0 0 1 0 5.5z"/></svg>123 Name Street, 000<br>Your City, 00000-000</li>
    </ul>
    <div class="person">
      <div class="person-name">FULL NAME</div>
      <div class="person-role">POSITION</div>
    </div>
    <svg class="front-bands" viewBox="0 0 840 120" preserveAspectRatio="none" aria-hidden="true">
      <defs>
        <linearGradient id="blueBand" x1="0" x2="1">
          <stop offset="0" stop-color="#0a6fbf"/><stop offset="1" stop-color="#1e8ad6"/>
        </linearGradient>
        <linearGradient id="navyBand" x1="0" x2="1">
          <stop offset="0" stop-color="#1c3344"/><stop offset="1" stop-color="#0b1c2b"/>
        </linearGradient>
      </defs>
      <polygon points="0,108 500,70 500,120 0,120" fill="url(#blueBand)"/>
      <polygon points="512,68 840,0 840,120 512,120" fill="url(#navyBand)"/>
    </svg>
  </section>

  <section class="card card-back">
    <span class="back-mark"></span>
    <div class="back-name">Kestrova</div>
    <div class="back-tagline">Electrical Solutions</div>
  </section>
</body>
</html>
```